Corvell Executive Search - New Business Card Design Project

We are an executive search firm called Corvell Executive Search based in the UK. We require a custom design for a business card. We're looking to convey a professional service to executives for executive search recruitment services. In terms of colours, we like dark blues and grays (maybe even silver incorporated somewhere if we go for a foiled type of card) but we're open to your artistic flare. See our current logo in attachments. We are totally open on design so long as the design is slick and professional.
Updates

Thanks for all your contributions of various designs. I have to say the quality of work has been amazing which is going to make our job quite difficult in the coming days on making a decision. Thanks to you all that have taken the time to submit designs thus far. We'll keep on reviewing and try to narrow down our selection as soon as possible.

Target Market(s)

Executive Search

Industry/Entity Type

Recruitment

Contact Information for Business Card

Corvell Executive Search,
Exclusively Sourcing & Hiring Senior Leaders
Dominic Haverley, Managing Director,
07742 318906
0117 468 2917
dominic@corvellexecutive.example
corvellexecutive.example
47 Linden Court, Marsh Lane, Bristol, BS9 7QT

Font styles to use
Sans Serif
Other font styles liked:
• Roboto (which is used in our logo)

Requirements
Must have
• Our logo (It has a subtle fade on it from #02071d at top to #333649 at bottom)
• The logo can be on one side or both sides
• Must be elegant and professional
• We have 2nd slogan CONSULT | INSPIRE | INNOVATE | DELIVER which can be incorporated into the card
Nice to have
• Use of blues and grey colours
• Compatible with similar styling to our website corvellexecutive.example
Should not have
• Must not be overly brash
• Must not contain cartoon characters

```html
<!DOCTYPE html>
<html lang="en">
<head>
<meta charset="utf-8">
<title>Corvell Executive Search – Business Card</title>
<link href="https://fonts.googleapis.com/css2?family=Open+Sans:wght@400;600;700&display=swap" rel="stylesheet">
<style>
  :root {
    --backdrop: #2b2b2d;
    --card-white: #f3f3f3;
    --navy: #0a1030;
    --navy-top: #02071d;
    --navy-bottom: #333649;
    --ink-grey: #4a4a4f;
    --rule: #3a3d4f;
    --silver: #d5d7de;
    --slogan: #e2e4ec;
  }
  * { margin: 0; padding: 0; box-sizing: border-box; }
  html, body {
    width: 1200px; height: 960px; overflow: hidden;
    background: var(--backdrop);
    font-family: "Open Sans", Arial, sans-serif;
  }
  .canvas { position: relative; width: 1200px; height: 960px; }

  .card {
    position: absolute;
    width: 520px; height: 324px;
    box-shadow: 2px 3px 6px rgba(0,0,0,.45);
  }
  .card--front { left: 354px; top: 122px; background: var(--card-white); }
  .card--back {
    left: 351px; top: 481px;
    background: linear-gradient(to bottom, var(--navy-top), var(--navy-bottom));
  }

  /* Front */
  .person { position: absolute; right: 23px; top: 24px; text-align: right; }
  .person__name { font-weight: 700; font-size: 17px; color: var(--navy); line-height: 20px; letter-spacing: .2px; }
  .person__title { font-weight: 400; font-size: 16px; color: var(--ink-grey); line-height: 20px; letter-spacing: .3px; }
  .person-bar { position: absolute; right: 0; top: 23px; width: 8px; height: 40px; background: var(--navy); }

  .wordmark { position: absolute; left: 26px; color: var(--navy); font-weight: 700; line-height: 1; }
  .card--front .wordmark { top: 148px; }
  .wordmark__name { display: block; font-size: 47px; letter-spacing: -.5px; }
  .wordmark__sub { display: block; font-size: 22.5px; letter-spacing: -.2px; margin-top: 0; }
  .card--front .tagline {
    position: absolute; left: 26px; top: 214px;
    font-size: 10px; font-weight: 600; color: var(--navy);
  }
  .rule { position: absolute; left: 26px; top: 235px; width: 466px; height: 1px; background: var(--rule); }

  .contact { position: absolute; left: 25px; top: 243px; color: var(--ink-grey); font-size: 14.5px; line-height: 19px; }
  .contact__row { white-space: nowrap; }
  .contact__label { font-weight: 700; color: var(--navy); }
  .contact__row--small { font-size: 13.5px; letter-spacing: -.2px; }

  /* Back */
  .card--back .wordmark { left: 112px; top: 122px; color: var(--silver); }
  .card--back .wordmark__name { font-size: 56px; }
  .card--back .wordmark__sub { font-size: 28.5px; margin-top: 1px; }
  .slogan {
    position: absolute; left: 0; right: 0; top: 274px;
    text-align: center; color: var(--slogan);
    font-size: 14px; letter-spacing: .6px; word-spacing: 2px;
  }
</style>
</head>
<body>
<main class="canvas">
  <section class="card card--front" aria-label="Business card front">
    <div class="person">
      <div class="person__name">DOMINIC HAVERLEY</div>
      <div class="person__title">MANAGING DIRECTOR</div>
    </div>
    <div class="person-bar"></div>

    <div class="wordmark">
      <span class="wordmark__name">CORVELL</span>
      <span class="wordmark__sub">EXECUTIVE SEARCH</span>
    </div>
    <div class="tagline">Exclusively Sourcing &amp; Hiring Senior Leaders</div>
    <div class="rule"></div>

    <div class="contact">
      <div class="contact__row">47 Linden Court, Marsh Lane, Bristol, BS9 7QT</div>
      <div class="contact__row"><span class="contact__label">P :</span> 07742 318906 <span class="contact__label">M :</span> 0117 468 2917</div>
      <div class="contact__row contact__row--small"><span class="contact__label">E :</span> dominic@corvellexecutive.example <span class="contact__label">W :</span> corvellexecutive.example</div>
    </div>
  </section>

  <section class="card card--back" aria-label="Business card back">
    <div class="wordmark">
      <span class="wordmark__name">CORVELL</span>
      <span class="wordmark__sub">EXECUTIVE SEARCH</span>
    </div>
    <div class="slogan">CONSULT &nbsp;|&nbsp; INSPIRE &nbsp;|&nbsp; INNOVATE &nbsp;|&nbsp; DELIVER</div>
  </section>
</main>
</body>
</html>
```